Need to design a business card with logo

Hellow
we are a company ,
PT REKA LINTAS MANDIRI
looking for design of name card.
what we do is property development and management.
design preferable professional corporate look and feel.
corporate. color, pantone colour 289
information required is
company name " Reka Lintas Mandiri"
person name eg " Peter Hollis"
person title eg "secret agent"
address: 9 kestrel road , jakarta, indonesia
phone : +6221 5906471
mobile : 0813 294 615
email : peter@hollistran.com
website: www.peterhol.com
if you want to include logo in the design you are welcome and appreciated , or you can simply use the company name as the logo.
thanks
corporate , business person , show events, exhibition events ,etc
Business

```html
<!DOCTYPE html>
<html lang="en">
<head>
<meta charset="utf-8">
<title>Reka Lintas Mandiri – Business Card</title>
<link rel="stylesheet" href="https://fonts.googleapis.com/css2?family=Raleway:wght@400;500;700&display=swap">
<style>
  :root {
    --stage: #0d0f14;
    --navy: #1f2e4c;
    --navy-deep: #18253f;
    --paper: #f4f5f6;
    --white: #f2f3f5;
    --steel: #a9b6c4;
    --icon-bg: #e6e8eb;
  }
  * { box-sizing: border-box; margin: 0; padding: 0; }
  html, body {
    width: 1200px; height: 1000px; overflow: hidden;
    background: var(--stage);
    font-family: "Raleway", sans-serif;
  }
  .stage { position: relative; width: 1200px; height: 1000px; }

  /* Front card – portrait, white */
  .card-front {
    position: absolute; left: 70px; top: 150px;
    width: 380px; height: 700px;
    background: var(--paper);
    overflow: hidden;
  }
  .card-front .brand-dot {
    position: absolute; left: 170px; top: 300px;
    width: 40px; height: 40px; border-radius: 50%;
    background: var(--navy);
  }
  .card-front .brand-name {
    position: absolute; left: 190px; top: 362px;
    transform-origin: 0 0; transform: rotate(90deg) translateY(-50%);
    white-space: nowrap;
    font-weight: 500; font-size: 20px; letter-spacing: 3px; line-height: 1;
    color: var(--navy);
  }

  /* Back card – landscape, navy */
  .card-back {
    position: absolute; left: 450px; top: 300px;
    width: 700px; height: 400px;
    background: linear-gradient(160deg, var(--navy) 0%, var(--navy-deep) 100%);
    color: var(--white);
    overflow: hidden;
  }
  .rule { position: absolute; top: 0; width: 6px; height: 250px; background: var(--white); }
  .rule-a { left: 52px; }
  .rule-b { left: 68px; }

  .person { position: absolute; left: 95px; top: 75px; width: 300px; }
  .person-name { font-weight: 700; font-size: 44px; line-height: 1; white-space: nowrap; }
  .person-name .surname { color: var(--steel); }
  .person-title {
    margin-top: 6px; text-align: right;
    font-weight: 500; font-size: 19px; color: var(--steel); letter-spacing: 0.5px;
    position: relative; left: -5px;
  }

  .brand { position: absolute; right: 60px; top: 60px; width: 170px; text-align: center; }
  .brand-ring {
    width: 150px; height: 150px; margin: 0 auto;
    border-radius: 50%; border: 8px solid var(--white);
  }
  .brand-label { margin-top: 12px; font-weight: 500; font-size: 15px; letter-spacing: 1px; color: var(--white); }

  .contacts { position: absolute; left: 46px; top: 258px; list-style: none; }
  .contacts li { display: flex; align-items: center; height: 45px; font-size: 19px; }
  .contacts .icon {
    width: 32px; height: 32px; border-radius: 50%; background: var(--icon-bg);
    display: flex; align-items: center; justify-content: center; margin-right: 18px;
  }
  .contacts svg { width: 18px; height: 18px; fill: var(--navy); }

  .email { position: absolute; right: 0; top: 314px; display: flex; align-items: center; font-size: 18px; }
  .email .icon {
    width: 26px; height: 26px; border-radius: 50%; background: var(--icon-bg);
    display: flex; align-items: center; justify-content: center; margin: 0 12px 0 14px;
  }
  .email .icon svg { width: 15px; height: 15px; fill: var(--navy); }
  .email .bars { display: flex; flex-direction: column; gap: 5px; }
  .email .bars span { display: block; width: 48px; height: 5px; background: var(--white); }
</style>
</head>
<body>
<main class="stage">

  <section class="card-front" aria-label="Card front">
    <span class="brand-dot"></span>
    <p class="brand-name">REKA LINTAS MANDIRI</p>
  </section>

  <section class="card-back" aria-label="Card back">
    <span class="rule rule-a"></span>
    <span class="rule rule-b"></span>

    <div class="person">
      <h1 class="person-name">Peter <span class="surname">Hollis</span></h1>
      <p class="person-title">SECRET AGENT</p>
    </div>

    <div class="brand">
      <div class="brand-ring"></div>
      <p class="brand-label">Reka Lintas Mandiri</p>
    </div>

    <ul class="contacts">
      <li>
        <span class="icon"><svg viewBox="0 0 24 24"><path d="M12 3 2 12h3v8h5v-5h4v5h5v-8h3z"/></svg></span>
        9 Kestrel Road , Jakarta, Indonesia
      </li>
      <li>
        <span class="icon"><svg viewBox="0 0 24 24"><path d="M6.6 10.8a15 15 0 0 0 6.6 6.6l2.2-2.2c.3-.3.7-.4 1-.2 1.1.4 2.3.6 3.6.6.6 0 1 .4 1 1V20c0 .6-.4 1-1 1A17 17 0 0 1 3 4c0-.6.4-1 1-1h3.5c.6 0 1 .4 1 1 0 1.3.2 2.5.6 3.6.1.3 0 .7-.2 1z"/></svg></span>
        +6221 5906471
      </li>
      <li>
        <span class="icon"><svg viewBox="0 0 24 24"><path d="M8 2h8a2 2 0 0 1 2 2v16a2 2 0 0 1-2 2H8a2 2 0 0 1-2-2V4a2 2 0 0 1 2-2zm0 3v12h8V5zm4 13.5a1 1 0 1 0 0 2 1 1 0 0 0 0-2z"/></svg></span>
        0813 294 615
      </li>
    </ul>

    <div class="email">
      peter@hollistran.com
      <span class="icon"><svg viewBox="0 0 24 24"><path d="M2 5h20v14H2zm2 2v.5l8 5 8-5V7zm0 2.8V17h16V9.8l-8 5z"/></svg></span>
      <span class="bars"><span></span><span></span></span>
    </div>
  </section>

</main>
</body>
</html>
```